BRAVEWELL DISPLAY GROUP Website

Looking for a website design that clearly and powerfully portrays our unique and effective indoor advertising billboards in our network.

Our TinyPlates, TallPlates and GrandFlags are strategically placed in high traffic areas of restaurants, pubs, nightclubs, fitness clubs, colleges and universities, and sports arenas.

Bravewell Display Group is our new name. Our current site is www.plovacorp.ca with our focus now being entirely on our Out-of-Home media. New website address will be www.bravewelldisplay.ca

We need the following sections:

HOME
PRODUCTS (Drop down menu)
-TinyPlates
-TallPlates
-GrandFlags
NETWORKS (Drop down menu)
-Dine-Pour
-Sports
-Campus
EFFECTIVENESS
CAMPAIGNS *This page will show numerous ad campaigns and could be a slide show (see www.plovacorp.ca/KVPL_campaigns.html )
BECOME A PARTNER
CONTACT

Please include social media functions on the homepage such as chirpnet/pagelink/workring

We will be supplying content and photos as required.

Our plan is to have you submit the homepage design to start with, and then we can start judging which styles we like the best and can start narrowing our list. As a second round, we would like to ask the "finalists" to submit a second page (another section of the website) and to see how consistent you are in terms of the look and feel you proposed for the homepage.

Attached is our new logo.

We may require you to upload the final website for us.

Websites that are in similar industry are:
www.torvelix.com
www.quandrafeed.com

Industry/Entity Type

Advertising

Requirements
Must have
• Our network offers advertising solutions that feature: Guaranteed Readership,100% Gender Specific, Frequency, and Captive Audience. Purchasing advertising space in our network are small to medium business owners and advertising agencies booking on behalf of their clients.

Site must be professional and modern looking.
Nice to have
• Moving banner or slide show of some type.

```html
<!DOCTYPE html>
<html lang="en">
<head>
<meta charset="utf-8">
<title>Bravewell Display Group – Tiny Plates</title>
<link rel="stylesheet" href="https://fonts.googleapis.com/css2?family=Ubuntu:wght@400;500;700&family=Arimo:wght@400&display=swap">
<style>
  :root {
    --brand-blue: #2a6bb5;
    --brand-blue-dark: #1f5aa0;
    --nav-top: #4a8ad6;
    --nav-bottom: #2262ad;
    --ink: #1c1c1c;
    --ink-soft: #3a3a3a;
    --grey-tab: #8a8a8a;
    --grey-drop: #7d7d7d;
    --grey-line: #a8a8a8;
    --side-bg: #c9c9c9;
    --side-border: #9a9a9a;
    --page-top: #ffffff;
    --page-bottom: #e1e1e1;
    --white: #ffffff;
  }
  * { margin: 0; padding: 0; box-sizing: border-box; }
  html, body { width: 1200px; height: 860px; overflow: hidden; }
  body {
    position: relative;
    background: linear-gradient(180deg, var(--page-top) 0%, #f2f2f2 40%, var(--page-bottom) 100%);
    font-family: "Arimo", Arial, sans-serif;
    color: var(--ink);
  }

  .brand {
    position: absolute; left: 46px; top: 40px;
    display: flex; align-items: center; gap: 12px;
  }
  .brand-square { width: 34px; height: 34px; background: var(--grey-tab); border-radius: 6px; }
  .brand-name {
    font-family: "Ubuntu", sans-serif; font-weight: 700; font-size: 27px;
    color: var(--brand-blue);
  }

  .header-contact {
    position: absolute; right: 76px; top: 28px; text-align: right;
    font-family: "Ubuntu", sans-serif;
  }
  .cta-title { font-size: 21px; font-weight: 500; color: var(--brand-blue); letter-spacing: 0.3px; }
  .call-line { margin-top: 4px; display: flex; justify-content: flex-end; align-items: baseline; gap: 20px; }
  .call-label { font-size: 16px; color: var(--ink); }
  .call-number { font-size: 23px; font-weight: 500; color: var(--ink); }

  .social {
    position: absolute; right: 76px; top: 94px;
    display: flex; gap: 12px; list-style: none;
    font-family: "Ubuntu", sans-serif; font-size: 12px; color: var(--brand-blue);
  }
  .social li { display: flex; align-items: center; gap: 4px; }
  .social-square { width: 12px; height: 12px; background: var(--brand-blue); border-radius: 2px; }

  .main-nav {
    position: absolute; left: 34px; top: 138px; width: 1130px; height: 47px;
    background: linear-gradient(180deg, var(--nav-top), var(--nav-bottom));
    border-radius: 4px; border: 1px solid var(--brand-blue-dark);
  }
  .main-nav ul { list-style: none; display: flex; height: 100%; padding-left: 26px; }
  .main-nav li {
    font-family: "Ubuntu", sans-serif; font-weight: 500; font-size: 17px;
    color: var(--white); display: flex; align-items: center; padding: 0 20px;
  }
  .main-nav li.is-active { background: linear-gradient(180deg, #9a9a9a, #7a7a7a); padding: 0 10px; margin: 0 10px; }

  .dropdown {
    position: absolute; left: 162px; top: 186px; width: 226px;
    background: var(--grey-drop); list-style: none; z-index: 2;
    box-shadow: 0 2px 4px rgba(0,0,0,0.25);
  }
  .dropdown li {
    height: 36px; line-height: 36px; padding-left: 24px;
    font-family: "Ubuntu", sans-serif; font-size: 15px; color: var(--white);
    border-bottom: 1px solid var(--grey-line);
  }
  .dropdown li:first-child { background: #939393; }
  .dropdown li:last-child { border-bottom: none; }

  .hero {
    position: absolute; left: 40px; top: 204px; width: 1120px; height: 338px;
    border-radius: 4px; border: 1px solid #bdbdbd;
    background: linear-gradient(90deg, #d9d2c6 0%, #e7e2d8 25%, #8a6a5a 32%, #c9c2b8 55%, #5b7a4c 78%, #d8d2c6 100%);
  }

  .breadcrumb { position: absolute; left: 44px; top: 558px; font-size: 13px; color: var(--ink); }

  .page-title {
    position: absolute; left: 44px; top: 584px;
    font-family: "Ubuntu", sans-serif; font-weight: 500; font-size: 31px; color: var(--brand-blue);
  }
  .page-copy {
    position: absolute; left: 44px; top: 626px; width: 821px;
    font-size: 14.4px; line-height: 19.2px; text-align: justify; color: var(--ink);
  }

  .side-nav {
    position: absolute; left: 904px; top: 593px; width: 258px;
    background: var(--side-bg); border: 1px solid var(--side-border); border-radius: 3px;
    list-style: none;
  }
  .side-nav li {
    height: 47px; line-height: 47px; padding-left: 17px;
    font-family: "Ubuntu", sans-serif; font-size: 16px; color: var(--ink-soft);
    border-bottom: 1px solid var(--side-border);
  }
  .side-nav li:last-child { border-bottom: none; }
  .side-nav li.is-current { color: var(--brand-blue); }

  .site-footer {
    position: absolute; left: 0; bottom: 0; width: 1200px; height: 46px;
    background: var(--brand-blue);
  }
  .copyright {
    position: absolute; right: 50px; top: 17px;
    font-size: 12.5px; color: var(--white);
  }
</style>
</head>
<body>
  <header>
    <div class="brand">
      <span class="brand-square"></span>
      <span class="brand-name">Bravewell Display Group</span>
    </div>
    <div class="header-contact">
      <div class="cta-title">START YOUR AD CAMPAIGN</div>
      <div class="call-line">
        <span class="call-label">CALL US</span>
        <span class="call-number">555-014-2290</span>
      </div>
    </div>
    <ul class="social">
      <li><span class="social-square"></span>pagelink</li>
      <li><span class="social-square"></span>chirpnet</li>
      <li><span class="social-square"></span>workring</li>
    </ul>
  </header>

  <nav class="main-nav">
    <ul>
      <li>HOME</li>
      <li class="is-active">PRODUCTS</li>
      <li>NETWORKS</li>
      <li>EFFECTIVENESS</li>
      <li>CAMPAIGNS</li>
      <li>BECOME A PARTNER</li>
      <li>CONTACT</li>
    </ul>
  </nav>
  <ul class="dropdown">
    <li>TINY PLATES</li>
    <li>TALL PLATES</li>
    <li>GRAND FLAGS</li>
  </ul>

  <div class="hero" role="img" aria-label="Photo of an indoor lobby with a wall-mounted display screen showing an advertisement, chairs and a potted palm"></div>

  <main>
    <div class="breadcrumb">Home &gt; Products &gt; Tiny Plates</div>
    <h1 class="page-title">Tiny Plates</h1>
    <p class="page-copy">Lorem ipsum dolor sit amet, has et ponderum deterruisset, quo porro accusam at, no paulo eleifend ocurreret duo. Vide audire ocurreret in est. Mei reque corpora at, ne eligendi facilisis vix, et vis putant interpretaris. No nec porro adipisci, sit nibh erat senserit no. Ferri accusamus mediocritatem vim at.Lorem ipsum dolor sit amet, has et ponderum deterruisset, quo porro accusam at, no paulo eleifend ocurreret duo. Vide audire ocurreret in est. Mei reque corpora at, ne eligendi facilisis vix, et vis putant interpretaris. No nec porro adipisci, sit nibh erat senserit no. Ferri accusamus mediocritatem vim at.</p>
    <ul class="side-nav">
      <li class="is-current">TINY PLATES</li>
      <li>TALL PLATES</li>
      <li>GRAND FLAGS</li>
    </ul>
  </main>

  <footer class="site-footer">
    <div class="copyright">Copyright 2012 Bravewell Display Group</div>
  </footer>
</body>
</html>
```